Liquor Label / Aguardiente

Label design for liquor bottle. Designers may submit multiple submissions.

Product Description:
Name: Viento de Plata™
Alcohol Category: Aguardiente (which in Spanish most closely translates to “burning water”) – aguardiente is derived from
cane sugar and is a general term for a type of alcoholic spirit in many Central and South America countries.
Taste: A smooth liquor with a comfortable yet spicy finish
Smell: Subtle aroma of spicy jalapeños
Liquid Color: Clear
Bottle Color: Clear
See link for reference - http://www.kelvostamp.com/sites/default/files/styles/uc_product_full/public/Pemrow_0.jpg?itok=9QmT2xLp
Closure: Bar top / cork
Bottle Shape/Size: height = 8.67in; diameter of base = 3.70in; diameter of neck = 0.85in

Label may consist of two separate parts (i.e. front and back, front and vertical side), or one continuous label.

Designer has complete freedom with color, font etc. unless otherwise stated below. The label MUST
contain (but is not limited only to) the following text exactly as written in quotes below:
- “Viento de Plata”
- “Aguardiente”
- “Cane Neutral Spirit with Natural Flavors”
- “35% Alc./Vol.”
- “750 ml”
- “Bottled by WP Spirits, LLC” and “Nashville, TN” - “Government Warning: (1) According to the Surgeon General, women should not drink alcoholic beverages during
pregnancy because of the risk of birth defects. (2) Consumption of alcoholic beverages impairs your ability to
drive a car or operate machinery, and may cause health problems.” (text in previous quotes must be in all
capitalized letters, text must be 2 MM in height and quote must be separated 2MM by all other text)
- Must be dedicated empty space for bar code (approximately 0.75in. height x 1.25in. length)

Target Market(s)

Label should have mass market appeal.
Age: 21 – 28 years old (primary target market is 21+ year old college students and recent graduates)
Target Market Gender: Both male and female, with emphasis on male
Consumption Focus: Spirit will be consumed typically as a shot, primarily at bars and secondarily off premise (label design will be critical for making our product highly visible behind a bar)
Marketing Theme: South American elements. The official Viento de Plata mascot is a llama and the incorporation and use of a llama somewhere (however large or small) on the bottle is encourage but by no means required.

Industry/Entity Type

Health

Requirements
Should not have
• Elements that may lead a potential consumer to believe the beverage is a craft liquor or an artisan brand. Please do not include images of peppers.

```html
<!DOCTYPE html>
<html lang="en">
<head>
<meta charset="utf-8">
<title>Viento de Plata – Aguardiente Labels</title>
<link rel="stylesheet" href="https://fonts.googleapis.com/css2?family=Francois+One&family=Marck+Script&family=Arimo:wght@400&display=swap">
<style>
  :root {
    --bg: #ffffff;
    --ink-white: #ffffff;
    --label-black: #1c1c1c;
    --label-grey: #2a2a2a;
    --fire-red: #d0121b;
    --mid-red: #a50d14;
    --deep-red: #4a0406;
    --gold: #f3b612;
    --script-grey: #d2d2d2;
    --stripe-red: #e0202a;
    --stripe-teal: #5fd3d6;
  }
  html, body {
    margin: 0;
    padding: 0;
    width: 1199px;
    height: 1200px;
    overflow: hidden;
    background: var(--bg);
  }
  .canvas {
    width: 1199px;
    height: 1200px;
    display: flex;
    justify-content: center;
    align-items: center;
    gap: 80px;
  }
  .label {
    position: relative;
    width: 420px;
    height: 450px;
    overflow: hidden;
    color: var(--ink-white);
  }
  .label p, .label h1 { margin: 0; }
  .label--red {
    background: radial-gradient(ellipse 75% 45% at 50% 48%, var(--fire-red) 0%, var(--mid-red) 40%, var(--deep-red) 72%, var(--label-black) 100%);
  }
  .label--black {
    background: linear-gradient(180deg, #252525 0%, var(--label-grey) 50%, #222222 100%);
  }
  .brand {
    position: absolute;
    left: 0;
    right: 0;
    top: 56px;
    text-align: center;
    font-family: "Francois One", "Arial Narrow", sans-serif;
    font-weight: 400;
    font-size: 92px;
    line-height: 1.02;
    color: var(--ink-white);
  }
  .category {
    position: absolute;
    left: 0;
    right: 0;
    top: 290px;
    text-align: center;
    font-family: "Marck Script", cursive;
    font-size: 24px;
    line-height: 1;
    transform: translateX(12px);
  }
  .label--red .category { color: var(--gold); }
  .label--black .category { color: var(--script-grey); }
  .descriptor {
    position: absolute;
    left: 0;
    right: 0;
    top: 322px;
    text-align: center;
    font-family: "Arimo", Arial, sans-serif;
    font-size: 16px;
    line-height: 1;
  }
  .specs {
    position: absolute;
    left: 18px;
    right: 40px;
    top: 378px;
    display: flex;
    justify-content: space-between;
    font-family: "Arimo", Arial, sans-serif;
    font-size: 15px;
    line-height: 1;
  }
  .stripes {
    position: absolute;
    left: 0;
    right: 0;
    top: 400px;
  }
  .stripe { height: 3px; margin-bottom: 4px; }
  .stripe--white { background: var(--ink-white); }
  .stripe--red { background: var(--stripe-red); }
  .stripe--teal { background: var(--stripe-teal); }
</style>
</head>
<body>
<main class="canvas">

  <section class="label label--red" aria-label="Viento de Plata label, red edition">
    <h1 class="brand">Viento<br>de Plata</h1>
    <p class="category">Aguardiente</p>
    <p class="descriptor">Cane Neutral Spirit with Natural Flavors</p>
    <div class="specs"><span>35% Alc./Vol</span><span>750 ml</span></div>
    <div class="stripes">
      <div class="stripe stripe--white"></div>
      <div class="stripe stripe--red"></div>
    </div>
  </section>

  <section class="label label--black" aria-label="Viento de Plata label, black edition">
    <h1 class="brand">Viento<br>de Plata</h1>
    <p class="category">Aguardiente</p>
    <p class="descriptor">Cane Neutral Spirit with Natural Flavors</p>
    <div class="specs"><span>35% Alc./Vol</span><span>750 ml</span></div>
    <div class="stripes">
      <div class="stripe stripe--teal"></div>
      <div class="stripe stripe--white"></div>
      <div class="stripe stripe--red"></div>
    </div>
  </section>

</main>
</body>
</html>
```